Electronic Music Artist needs an Album Cover

DRELL is an electronic musician from Boston, Massachusetts. He needs an album cover that captures the essence of his music. The album is called Lanterns, which represents his experiences growing up, positive and negative. He would like to see designs that involves color and creativity. Attached are some examples of artworks that DRELL likes. He also included a few of his original photos (optional to use. Using a photo will not effect his final decision!), and his logo.

Colors

Designer to choose colors to be used in the design.

Requirements
Must have
• My project must have the text "Lanterns" and "DRELL", and the logo (attached in the files). The logo should not be the main subject of the artwork. Everything must look aesthetically pleasing.
Nice to have
• It would be nice to have some sort of creative graphic design (see example album covers for reference). Also, in one of the references, there is a column on the left hand side with some text in it. That could be cool to include, but without the asian text.
Should not have
• The project should not have any other language besides English.

```html
<!DOCTYPE html>
<html lang="en">
<head>
<meta charset="utf-8">
<title>DRELL — Lanterns</title>
<link rel="stylesheet" href="https://fonts.googleapis.com/css2?family=Arimo:wght@700&family=Kaushan+Script&display=swap">
<style>
  :root {
    --ink-deep: #150d40;
    --ink-violet: #2b1585;
    --mark-grey: #a6a3ae;
    --holo-violet: #8a5cf0;
    --holo-lilac: #b9a2f2;
    --holo-teal: #7fe0d0;
    --holo-lime: #c6e86a;
    --holo-gold: #e8c46a;
    --holo-magenta: #c85ad8;
    --holo-blue: #5a5cf0;
  }
  html, body {
    margin: 0;
    padding: 0;
    width: 1200px;
    height: 1200px;
    overflow: hidden;
    background: #ffffff;
  }
  .cover {
    position: relative;
    width: 1200px;
    height: 1200px;
    overflow: hidden;
  }
  .cover__artwork {
    position: absolute;
    inset: 0;
    background:
      linear-gradient(90deg, transparent 0 488px, rgba(200, 215, 255, 0.18) 488px 100%),
      radial-gradient(ellipse 420px 260px at 1000px 300px, rgba(200, 90, 216, 0.45), transparent 70%),
      radial-gradient(ellipse 380px 220px at 900px 900px, rgba(127, 224, 208, 0.45), transparent 70%),
      linear-gradient(150deg,
        var(--holo-blue) 0%,
        var(--holo-lime) 14%,
        var(--holo-gold) 22%,
        var(--holo-teal) 32%,
        var(--holo-violet) 42%,
        var(--holo-lilac) 52%,
        var(--holo-teal) 62%,
        var(--holo-violet) 72%,
        var(--holo-magenta) 82%,
        var(--holo-lilac) 100%);
  }
  .cover__mark {
    position: absolute;
    top: 92px;
    right: 88px;
    font-family: "Arimo", Arial, sans-serif;
    font-weight: 700;
    font-size: 34px;
    letter-spacing: 2px;
    color: var(--mark-grey);
  }
  .cover__title {
    position: absolute;
    left: 0;
    right: 0;
    top: 486px;
    text-align: center;
  }
  .cover__artist {
    display: block;
    margin: 0 0 0 -4px;
    font-family: "Arimo", Arial, sans-serif;
    font-weight: 700;
    font-size: 160px;
    line-height: 160px;
    color: var(--ink-deep);
  }
  .cover__album {
    display: block;
    margin: -6px 0 0 8px;
    font-family: "Kaushan Script", cursive;
    font-size: 74px;
    line-height: 90px;
    color: var(--ink-violet);
  }
</style>
</head>
<body>
  <main class="cover">
    <div class="cover__artwork" role="img" aria-label="Abstract holographic artwork of flowing diagonal light streaks in violet, teal, lime and gold with marbled magenta textures"></div>
    <div class="cover__mark">DRELL</div>
    <h1 class="cover__title">
      <span class="cover__artist">DRELL</span>
      <span class="cover__album">Lanterns</span>
    </h1>
  </main>
</body>
</html>
```